Business Coaching Model and Flow Chart

We need this flowchart, attached, to be updated in a modern and engaging way. This flowchart is the cornerstone of a business coaching class we are running, and will be the main support reference for the people who take the class. We are open to ideas as to how it is presented, but we would like a largely minimalist look that leaves space to be impactful where the key information sites. Our colour scheme is primary red (D51C29), white, grey (333333), black, and secondary green (3C8740). We will also need our logo present (attached).

```html
<!DOCTYPE html>
<html lang="en">
<head>
<meta charset="utf-8">
<title>Group to Teams Through Learning Together</title>
<link href="https://fonts.googleapis.com/css2?family=Fira+Sans:wght@400;500;600&family=Fira+Sans+Condensed:wght@600;700&display=swap" rel="stylesheet">
<style>
  :root{
    --red:#d51c29;
    --grey:#333333;
    --ink:#222222;
    --white:#ffffff;
  }
  *{box-sizing:border-box;margin:0;padding:0}
  html,body{width:1200px;height:675px;overflow:hidden;background:var(--white)}
  body{position:relative;font-family:"Fira Sans",Arial,sans-serif;color:var(--ink)}

  .brand{position:absolute;left:18px;top:21px;width:90px;text-align:center}
  .brand-mark{width:77px;height:77px;border-radius:50%;background:var(--red);margin:0 auto}
  .brand-name{margin-top:5px;font-family:"Fira Sans Condensed",sans-serif;font-weight:700;font-size:9.5px;color:var(--red);letter-spacing:.3px;text-transform:uppercase}

  .title-band{position:absolute;left:125px;top:19px;width:1075px;height:93px;background:var(--red);padding:10px 0 0 19px}
  .title-band h1{font-family:"Fira Sans Condensed",sans-serif;font-weight:700;font-size:31px;line-height:36px;color:var(--white);text-transform:uppercase;letter-spacing:.2px}

  .process{position:absolute;left:59px;top:142px;width:1082px;height:62px}
  .process svg{position:absolute;inset:0;width:100%;height:100%}
  .step{position:absolute;top:0;height:62px;width:154px;display:flex;flex-direction:column;justify-content:center;align-items:center;text-align:center;color:var(--white);font-family:"Fira Sans Condensed",sans-serif;font-weight:600;font-size:10.5px;line-height:13.5px;text-transform:uppercase}
  .step em{text-transform:none;font-style:italic}

  .col{position:absolute;top:235px;height:426px;border:1.3px solid var(--red);padding:18px 10px 0 19px;font-size:10.4px}
  .col.dark{background:var(--grey);border-color:var(--grey)}
  .col.solution{background:var(--red)}
  .list{list-style:none;display:flex;flex-direction:column;gap:23px;font-weight:500;line-height:13px}
  .sub{list-style:none;font-weight:400;margin-top:5px}
  .sub li{line-height:19px;padding-left:8px;position:relative}
  .sub li::before{content:"•";position:absolute;left:0}
  .sub.indent li{padding-left:8px}

  .icon-list{list-style:none;display:flex;flex-direction:column;align-items:center;gap:0;padding-top:0}
  .icon-item{height:50px;display:flex;flex-direction:column;align-items:center;justify-content:flex-start;color:var(--white);font-weight:500;font-size:10.2px;text-align:center;line-height:13px}
  .icon-item svg{width:20px;height:20px;margin-bottom:3px}
</style>
</head>
<body>

<div class="brand">
  <div class="brand-mark"></div>
  <div class="brand-name">Mara Ellison</div>
</div>

<header class="title-band">
  <h1>Group to Teams<br>Through Learning Together</h1>
</header>

<div class="process">
  <svg viewBox="0 0 1730 100" preserveAspectRatio="none" aria-hidden="true">
    <polygon points="0,0 217,0 267,50 217,100 0,100" fill="#333333"/>
    <polygon points="217,0 467,0 517,50 467,100 217,100 267,50" fill="#4a2d30"/>
    <polygon points="467,0 717,0 767,50 717,100 467,100 517,50" fill="#5f2a2f"/>
    <polygon points="717,0 967,0 1017,50 967,100 717,100 767,50" fill="#78262e"/>
    <polygon points="967,0 1217,0 1267,50 1217,100 967,100 1017,50" fill="#92232d"/>
    <polygon points="1217,0 1467,0 1517,50 1467,100 1217,100 1267,50" fill="#ad1f2b"/>
    <polygon points="1467,0 1730,0 1730,100 1467,100 1517,50" fill="#d51c29"/>
    <g fill="none" stroke="#fff" stroke-width="3">
      <polyline points="217,0 267,50 217,100"/>
      <polyline points="467,0 517,50 467,100"/>
      <polyline points="717,0 767,50 717,100"/>
      <polyline points="967,0 1017,50 967,100"/>
      <polyline points="1217,0 1267,50 1217,100"/>
      <polyline points="1467,0 1517,50 1467,100"/>
    </g>
  </svg>
  <div class="step" style="left:0">Problem</div>
  <div class="step" style="left:156px">Clarify<br>Challenges -<br>Diagnostics</div>
  <div class="step" style="left:312px">Planning<br>for Success<br><em>Make a Plan</em></div>
  <div class="step" style="left:468px">Learn<br>the Tools<br><span style="text-transform:none">Workshops</span></div>
  <div class="step" style="left:624px">Doing<br><em>Mastering<br>the Tools</em></div>
  <div class="step" style="left:780px">Reflect<br>Adapt<br>Embed</div>
  <div class="step" style="left:944px">Solution</div>
</div>

<section class="col dark" style="left:58px;width:146px;padding:8px 0 0">
  <ul class="icon-list">
    <li class="icon-item"><svg viewBox="0 0 20 20"><rect x="5" y="2" width="10" height="16" rx="1" fill="#fff"/><g stroke="#333" stroke-width="1.2"><line x1="7" y1="11" x2="13" y2="11"/><line x1="7" y1="14" x2="13" y2="14"/></g></svg>Underbilling</li>
    <li class="icon-item"><svg viewBox="0 0 20 20" fill="#fff"><circle cx="5" cy="6" r="2.2"/><circle cx="10" cy="5" r="2.5"/><circle cx="15" cy="6" r="2.2"/><rect x="2" y="9" width="16" height="7" rx="3"/></svg>Staff Retention</li>
    <li class="icon-item"><svg viewBox="0 0 20 20" fill="none" stroke="#fff" stroke-width="1.6"><circle cx="8" cy="8" r="5.5"/><line x1="12" y1="12" x2="18" y2="18"/></svg>Hard to Recruit</li>
    <li class="icon-item"><svg viewBox="0 0 20 20"><path d="M3 3h14v11h-5l-2 3-2-3H3z" fill="#fff"/><rect x="9.3" y="5" width="1.4" height="5" fill="#333"/><rect x="9.3" y="11" width="1.4" height="1.4" fill="#333"/></svg>Client Complaints</li>
    <li class="icon-item"><svg viewBox="0 0 20 20"><circle cx="10" cy="10" r="8" fill="#fff"/><path d="M6.5 14q3.5-3 7 0" stroke="#333" stroke-width="1.3" fill="none"/></svg>Staff Stress &amp; Burnout</li>
    <li class="icon-item"><svg viewBox="0 0 20 20" fill="none" stroke="#fff" stroke-width="1.4"><path d="M2 10h6M12 10h6M10 2v5M10 13v5M4 4l4 4M16 16l-4-4M16 4l-4 4M4 16l4-4"/></svg>Conflict</li>
    <li class="icon-item"><svg viewBox="0 0 20 20" fill="none" stroke="#fff" stroke-width="1.6"><path d="M16 8a6.5 6.5 0 0 0-12-1M4 12a6.5 6.5 0 0 0 12 1"/><path d="M4 3v4h4M16 17v-4h-4"/></svg>NDIS Constant Change</li>
    <li class="icon-item" style="margin-top:6px"><svg viewBox="0 0 20 20" fill="none" stroke="#fff" stroke-width="1.6"><path d="M5 2h10M5 18h10M6 2q0 6 4 8q-4 2-4 8M14 2q0 6-4 8q4 2 4 8"/></svg>Limited in Best Practice</li>
  </ul>
</section>

<section class="col" style="left:216px;width:144px">
  <ul class="list">
    <li>Scoping</li>
    <li>Interviews</li>
    <li>Group Reflection</li>
    <li>Opinion Surveys</li>
    <li>Certified Assessments
      <ul class="sub">
        <li>Personality Styles</li>
        <li>Work Preference</li>
        <li>Strengths &amp; Values</li>
        <li>Trust</li>
        <li>360</li>
      </ul>
    </li>
  </ul>
</section>

<section class="col" style="left:372px;width:144px;padding-left:14px">
  <ul class="list">
    <li>Team Data Analysis<br>Workshop</li>
    <li>Individual Development<br>Plan</li>
    <li>Team Development Plan</li>
    <li>Organizational Plan</li>
  </ul>
</section>

<section class="col" style="left:528px;width:144px;padding-left:14px">
  <ul class="list" style="gap:14px">
    <li>Foundation Workshops
      <ul class="sub">
        <li>Difficult Conversations</li>
        <li>Giving &amp; Receiving<br>Feedback</li>
        <li>Values Alignment</li>
        <li>Shared Purpose</li>
        <li>Ways of Working</li>
        <li>Diversity</li>
        <li>Wellbeing</li>
        <li>Time Management</li>
      </ul>
    </li>
    <li>Customised Workshops</li>
  </ul>
</section>

<section class="col" style="left:684px;width:144px;padding-left:24px">
  <ul class="list">
    <li>Group Coaching</li>
    <li>Team Coaching</li>
    <li>Individual Coaching</li>
    <li>Peer Learning</li>
    <li>Lunch ‘n Learn</li>
  </ul>
</section>

<section class="col" style="left:841px;width:144px;padding-left:8px">
  <ul class="list">
    <li>Culture Committee</li>
    <li>Embedding Workshop</li>
    <li>Culture Collateral</li>
    <li>WOW Manifesto</li>
    <li>Leadership Team Coaching</li>
    <li>Measure ROI</li>
    <li>Review Success</li>
    <li>Evaluation Surveys</li>
    <li>Temperature Checks</li>
    <li>Recruit to Suit</li>
    <li>Future Proofing -<br>What Next?</li>
  </ul>
</section>

<section class="col solution" style="left:996px;width:146px;padding:8px 0 0">
  <ul class="icon-list">
    <li class="icon-item"><svg viewBox="0 0 20 20" fill="#fff"><circle cx="10" cy="5" r="3.5"/><rect x="5" y="10" width="10" height="9" rx="4"/></svg>Self Awareness &amp; Ownership</li>
    <li class="icon-item"><svg viewBox="0 0 20 20" fill="#fff"><path d="M2 9l5-4 3 2 3-2 5 4-6 6z"/></svg>Partnership</li>
    <li class="icon-item"><svg viewBox="0 0 20 20" fill="#fff"><circle cx="5" cy="5" r="2"/><circle cx="10" cy="4" r="2"/><circle cx="15" cy="5" r="2"/><rect x="2" y="9" width="16" height="3"/><rect x="3" y="13" width="14" height="5"/></svg>Great Place to Work</li>
    <li class="icon-item"><svg viewBox="0 0 20 20" fill="#fff"><path d="M10 2l2 6-2 3-2-3zM3 7l6 4-1 3zM17 7l-6 4 1 3z"/><rect x="6" y="15" width="8" height="3"/></svg>Growth Mindset</li>
    <li class="icon-item"><svg viewBox="0 0 20 20" fill="#fff"><path d="M3 8h4l8-5v14l-8-5H3z"/><rect x="5" y="12" width="3" height="5"/></svg>Coach Approach Culture</li>
    <li class="icon-item"><svg viewBox="0 0 20 20"><path d="M2 4h16v10h-6l-2 3-2-3H2z" fill="#fff"/><g fill="#d51c29"><circle cx="6" cy="9" r="1.4"/><circle cx="10" cy="9" r="1.4"/><circle cx="14" cy="9" r="1.4"/></g></svg>Feedback Culture</li>
    <li class="icon-item"><svg viewBox="0 0 20 20" fill="none" stroke="#fff" stroke-width="2"><circle cx="8" cy="8" r="4"/><line x1="11" y1="11" x2="17" y2="17"/></svg>Way to Manage Conflict</li>
    <li class="icon-item" style="margin-top:6px"><svg viewBox="0 0 20 20" fill="#fff"><rect x="2" y="3" width="13" height="9"/><path d="M5 12v3l3-3zM16 7h2v8h-3l-2 2v-2H7v-2h9z"/></svg>Best Practice<br>Communication Skills</li>
  </ul>
</section>

</body>
</html>
```